Shadows over Briarwick Hall

We are hosting an open-to-the-public murder mystery dinner and masquerade ball on Oct. 31. I need a postcard design that we can display, hand out and mail for marketing.

We produce events in the KC area.

I'd like to see designs with a Halloween masquerade ball/murder mystery theme.

```html
<!DOCTYPE html>
<html lang="en">
<head>
<meta charset="utf-8">
<title>Shadows over Briarwick Hall — October 31st</title>
<link rel="stylesheet" href="https://fonts.googleapis.com/css2?family=Creepster&family=Montserrat:wght@400;600;700&display=swap">
<style>
  :root {
    --ink: #000000;
    --blood: #d8262b;
    --bone: #ffffff;
    --lime: #a4cf4a;
    --lime-deep: #6fae2e;
    --moon-light: #ececec;
    --moon-mid: #c9c9c9;
    --moon-shade: #9a9a9a;
    --feather: #2e2e2e;
    --feather-deep: #161616;
    --mask-silver: #bdbdbd;
    --mask-silver-deep: #6f6f6f;
    --mask-gold: #d08f45;
    --mask-gold-deep: #7a4a1c;
    --badge: #141a18;
  }
  * { margin: 0; padding: 0; box-sizing: border-box; }
  html, body { width: 1200px; height: 930px; overflow: hidden; background: var(--ink); }
  .postcard {
    position: relative;
    width: 1200px;
    height: 930px;
    background: var(--ink);
    overflow: hidden;
    font-family: "Montserrat", Arial, sans-serif;
    color: var(--bone);
  }
  .moon {
    position: absolute;
    left: 700px;
    top: -10px;
    width: 575px;
    height: 575px;
    border-radius: 50%;
    background: radial-gradient(circle at 42% 38%, var(--moon-light) 0%, var(--moon-mid) 50%, var(--moon-shade) 100%);
  }
  .brand {
    position: absolute;
    left: 925px;
    top: 52px;
    width: 220px;
    height: 190px;
    display: flex;
    align-items: center;
    justify-content: center;
  }
  .brand-disc {
    position: absolute;
    inset: 0;
    border-radius: 50%;
    background: var(--badge);
  }
  .brand-name {
    position: relative;
    font-weight: 600;
    font-size: 28px;
    color: var(--bone);
    white-space: nowrap;
  }
  .title {
    position: absolute;
    left: 40px;
    top: 48px;
    width: 680px;
    text-align: center;
    font-family: "Creepster", Georgia, cursive;
    font-weight: 400;
    line-height: 1;
  }
  .title-lead { display: block; color: var(--blood); font-size: 132px; }
  .title-join { display: block; color: var(--bone); font-size: 78px; margin-top: 4px; }
  .title-place { display: block; color: var(--lime); font-size: 100px; margin-top: 2px; }
  .masks {
    position: absolute;
    left: 40px;
    top: 390px;
    width: 770px;
    height: 280px;
    background:
      radial-gradient(ellipse 95px 60px at 272px 220px, var(--mask-silver) 0%, var(--mask-silver) 45%, var(--mask-silver-deep) 75%, transparent 100%),
      radial-gradient(ellipse 95px 60px at 462px 220px, var(--mask-gold) 0%, var(--mask-gold) 45%, var(--mask-gold-deep) 75%, transparent 100%),
      radial-gradient(ellipse 130px 150px at 272px 130px, var(--feather) 0%, transparent 100%),
      radial-gradient(ellipse 130px 150px at 462px 130px, var(--feather) 0%, transparent 100%),
      radial-gradient(ellipse 385px 140px at 385px 150px, var(--feather-deep) 0%, transparent 100%);
  }
  .date {
    position: absolute;
    left: 120px;
    top: 712px;
    width: 990px;
    display: flex;
    justify-content: space-between;
    font-size: 44px;
    font-weight: 400;
    white-space: nowrap;
    line-height: 1;
  }
  .date-month { color: var(--bone); letter-spacing: 0.66em; }
  .date-day { color: var(--lime); letter-spacing: 0.66em; margin-right: -0.66em; }
  .contact {
    position: absolute;
    left: 0;
    top: 784px;
    width: 1200px;
    text-align: center;
    line-height: 1.3;
  }
  .web { font-size: 25px; color: var(--bone); padding-left: 50px; }
  .web-name { color: var(--lime-deep); }
  .address { font-size: 22px; word-spacing: 9px; margin-top: 2px; padding-left: 20px; }
  .phone {
    display: inline-flex;
    align-items: center;
    gap: 6px;
    margin-top: 4px;
    margin-left: 50px;
    font-size: 30px;
    font-weight: 700;
  }
  .phone svg { width: 32px; height: 32px; }
</style>
</head>
<body>
<main class="postcard">
  <div class="moon" role="img" aria-label="Full moon with a flock of bats flying across it"></div>

  <div class="brand">
    <span class="brand-disc"></span>
    <span class="brand-name">Nocturne KC</span>
  </div>

  <h1 class="title">
    <span class="title-lead">Shadows</span>
    <span class="title-join">Over</span>
    <span class="title-place">Briarwick Hall</span>
  </h1>

  <div class="masks" role="img" aria-label="Two ornate feathered masquerade masks, one silver and one gold, facing each other against black plumes"></div>

  <p class="date"><span class="date-month">OCTOBER</span><span class="date-day">31ST&nbsp;&nbsp;2014</span></p>

  <div class="contact">
    <p class="web">www.<span class="web-name">NocturneKC</span>.com</p>
    <p class="address">The Terrace at Oakridge 2150 N Linden Dr. Kansas City, MO 64119</p>
    <p class="phone">
      <svg viewBox="0 0 32 32" aria-hidden="true">
        <circle cx="16" cy="16" r="14" fill="none" stroke="#6fae2e" stroke-width="2.5"/>
        <path d="M11 9.5c1-.8 2-.6 2.6.4l1.2 2c.5.9.3 1.8-.5 2.4l-.8.6c.8 1.8 2 3.1 3.7 4l.7-.8c.6-.8 1.6-.9 2.4-.4l2 1.2c1 .6 1.1 1.7.3 2.6-1.6 1.7-3.6 1.8-6 .4-3.3-2-5.3-4.8-6.1-8-.4-1.9 0-3.3.5-4.4z" fill="#6fae2e"/>
      </svg>
      816-555-0147
    </p>
  </div>
</main>
</body>
</html>
```